Need a banner for trees, and shrubs at our lanscape supply yard see attached logo

Need a nice banner to showcase our new addition of trees and shrubs for our customers.

```html
<!DOCTYPE html>
<html lang="en">
<head>
<meta charset="UTF-8">
<title>Ridgeline Supply – Trees &amp; Shrubs Banner</title>
<link href="https://fonts.googleapis.com/css2?family=Poppins:wght@600;700;800&family=Ultra&display=swap" rel="stylesheet">
<style>
  :root {
    --maroon: #6b1e22;
    --green: #1e9a45;
    --paper: #f2f0ec;
    --paper-shade: #e4e1dc;
    --page: #ffffff;
    --foliage-light: #9fd25a;
    --foliage-dark: #3f7a34;
    --stone: #d9d0c6;
    --bloom: #c9415f;
  }
  * { margin: 0; padding: 0; box-sizing: border-box; }
  html, body {
    width: 934px; height: 1200px; overflow: hidden;
    background: var(--page);
  }
  .banner {
    position: absolute; left: 37px; top: 385px;
    width: 860px; height: 430px; overflow: hidden;
    background: radial-gradient(ellipse at 30% 30%, var(--paper) 40%, var(--paper-shade) 100%);
    box-shadow: 0 14px 40px rgba(0,0,0,0.22);
    font-family: "Poppins", sans-serif;
  }
  .brand {
    position: absolute; left: 26px; top: 30px;
    display: flex; align-items: center; gap: 12px;
  }
  .brand-dot {
    width: 46px; height: 46px; border-radius: 50%;
    background: var(--green);
  }
  .brand-name {
    font-family: "Poppins", sans-serif; font-weight: 800;
    color: var(--maroon); font-size: 30px; line-height: 1.0;
    letter-spacing: 1px;
  }
  .headline {
    position: absolute; left: 22px; top: 118px;
    font-family: "Ultra", serif; font-size: 98px; line-height: 1;
    color: var(--maroon); letter-spacing: -2px;
  }
  .subhead {
    position: absolute; left: 22px; top: 218px;
    display: flex; align-items: center; gap: 14px;
    font-family: "Ultra", serif; font-size: 52px; line-height: 1;
    color: var(--green); letter-spacing: -1px;
  }
  .subhead-rules { display: flex; flex-direction: column; gap: 6px; }
  .subhead-rules span { display: block; width: 66px; height: 4px; background: var(--green); }
  .tagline {
    position: absolute; left: 25px; top: 284px;
    font-weight: 700; font-size: 20px; color: #1d1d1d;
    letter-spacing: -0.3px;
  }
  .phone-band {
    position: absolute; left: 0; top: 320px;
    width: 540px; height: 52px; background: var(--maroon);
    display: flex; align-items: center; padding-left: 22px; gap: 12px;
  }
  .phone-band svg { width: 32px; height: 32px; }
  .phone-number {
    font-weight: 700; font-size: 44px; color: #fff; letter-spacing: 1px;
    line-height: 1;
  }
  .web {
    position: absolute; left: 25px; top: 382px;
    font-weight: 700; font-size: 24px; letter-spacing: 3px; color: var(--green);
  }
  .web .dark { color: var(--maroon); }
  .photo { position: absolute; left: 0; top: 0; width: 860px; height: 430px; }
</style>
</head>
<body>
  <section class="banner">
    <div class="brand">
      <span class="brand-dot"></span>
      <span class="brand-name">RIDGELINE<br>SUPPLY</span>
    </div>

    <h1 class="headline">TREES</h1>
    <div class="subhead">
      <span>&amp; SHRUBS</span>
      <span class="subhead-rules"><span></span><span></span><span></span></span>
    </div>
    <p class="tagline">AT OUR LANSCAPE SUPPLY YARD</p>

    <div class="phone-band">
      <svg viewBox="0 0 24 24" aria-hidden="true">
        <path fill="#fff" d="M6.6 10.8a15.1 15.1 0 0 0 6.6 6.6l2.2-2.2a1 1 0 0 1 1-.25 11.4 11.4 0 0 0 3.6.57 1 1 0 0 1 1 1V20a1 1 0 0 1-1 1A17 17 0 0 1 3 4a1 1 0 0 1 1-1h3.5a1 1 0 0 1 1 1c0 1.25.2 2.45.57 3.57a1 1 0 0 1-.25 1z"/>
        <path fill="none" stroke="#fff" stroke-width="1.8" stroke-linecap="round" d="M14.5 3.5a6.5 6.5 0 0 1 6 6M14.5 7a3 3 0 0 1 2.6 2.6"/>
      </svg>
      <span class="phone-number">555-218-4730</span>
    </div>

    <p class="web"><span class="dark">WWW.</span>RIDGELINESUPPLY<span class="dark">.COM</span></p>

    <svg class="photo" viewBox="0 0 860 430" role="img" aria-label="Photo of a curving stone garden path lined with green shrubs and red-leaf plants">
      <defs>
        <linearGradient id="gardenTones" x1="0" y1="0" x2="1" y2="1">
          <stop offset="0" stop-color="var(--foliage-light)"/>
          <stop offset="0.35" stop-color="var(--foliage-dark)"/>
          <stop offset="0.6" stop-color="var(--stone)"/>
          <stop offset="1" stop-color="#c9c0b6"/>
        </linearGradient>
      </defs>
      <path d="M563 -4 Q 420 230 558 434 L 864 434 L 864 -4 Z" fill="url(#gardenTones)" stroke="var(--maroon)" stroke-width="5"/>
    </svg>
  </section>
</body>
</html>
```